Rather Likely The Brightest Venture
Website for Life Coach
Rather Likely The Brightest Venture - Personal Care
Creative Brief
Personal Care
www.bluelanternhour.com
Website design for inspirational and motivational training company. Initial focus of the website is to promote trainer for life coach and inspirational speaker engagements with plan to expend into seminar and web based trainings in 2013.
General feel to be very upbeat, happy, feel good, simple and easy to navigate. !!When referring to the holding page of Blue Lantern Hour (which I think looks crap) please note the writing in the Logo of the name should be in Black!!
left side
http://www.quostelbury.com/
http://www.drwabble.com/
http://www.nora-pellham.com/
Home page to include areas for the following: Top banner showing logo, quote and small picture of face of company. Below this a thicker banner with sunflower field picture (in future to be a video link) and beside it text of an inspirational quote that will change on a regular basis. This to also include an opt in button where they can provide email address to be contacted or receive blogs and articles direct to their account. Links to other pages: home, the way, live it, who is he, contact me, archive Home page to also include a Short text intro to what blue lantern hour is all about with a picture of face of company again. Below this Space for most recent blog or article in full (to be changed on a regular basis) Opt in button at bottom of page Links at bottom of page to affiliated websites The opt in button to be at top and bottom of all pages with affiliate web links at bottom of all pages. Additional pages: The Way: A page describing the lifestyle being coached and it's different sections. There are 6 text sections in total on this page, each with a matching inspirational image to it. Live It: Introducing the concept of coaching. Images and text again with one testimonial at the top and a list of testimonials at the bottom Who Is He: A simply text and images page for bio information Contact: listing of ways in which to contact me. Also a space where they can fill out name, contact, and question or request. The submit button will automatically send this to an email. Archive: a simple listing of previous blogs and articles. These to be listed at top with a click on link to where they are further down the page

```html
<!DOCTYPE html>
<html lang="en">
<head>
<meta charset="utf-8">
<title>Blue Lantern Hour</title>
<link rel="stylesheet" href="https://fonts.googleapis.com/css2?family=Arimo:wght@400;700&family=Roboto+Condensed:ital,wght@0,700;1,700&display=swap">
<style>
:root{
  --sun:#f7e21a;
  --sun-deep:#f1cf0c;
  --leaf:#6cae12;
  --leaf-light:#8cc63f;
  --leaf-dark:#2f6a06;
  --leaf-panel:#3d7a0b;
  --ink:#444;
  --muted:#888;
  --night:#0d0d0d;
  --white:#fff;
}
*{box-sizing:border-box;margin:0;padding:0}
html,body{width:1200px;height:1027px;overflow:hidden}
body{position:relative;background:radial-gradient(circle at 50% 30%,var(--sun) 0%,var(--sun-deep) 100%);font-family:"Arimo",Arial,sans-serif;color:var(--ink)}
.abs{position:absolute}
.site-footer{left:0;top:896px;width:1200px;height:131px;background:var(--night)}
.page{left:173px;top:28px;width:852px;height:882px;background:var(--white);border-radius:6px;box-shadow:0 0 0 5px rgba(255,255,255,.55),0 4px 12px rgba(0,0,0,.25)}
.brand{left:217px;top:56px;display:flex;align-items:center;gap:10px}
.brand-dot{width:62px;height:62px;border-radius:50%;background:var(--sun-deep)}
.brand-name{font:700 30px "Arimo",Arial,sans-serif;color:var(--leaf-dark)}
.account{top:52px;height:18px;padding:0 10px;border-radius:4px;background:linear-gradient(var(--leaf-light),var(--leaf));color:var(--white);font:700 10px "Arimo",Arial,sans-serif;line-height:18px;text-transform:uppercase}
.nav{left:184px;top:148px;width:832px;height:33px;display:flex;background:linear-gradient(var(--leaf-light),var(--leaf))}
.nav a{display:block;height:33px;line-height:33px;text-align:center;color:var(--white);text-decoration:none;font:700 13px "Roboto Condensed",Arial Narrow,sans-serif;text-transform:uppercase;border-right:1px solid rgba(255,255,255,.35)}
.nav a.active{background:var(--leaf-dark)}
.hero{left:184px;top:181px;width:832px;height:273px;background:linear-gradient(var(--leaf-light) 0%,var(--leaf) 70%,var(--leaf-dark) 100%)}
.hero-photo{left:264px;top:190px;width:223px;height:264px;background:linear-gradient(#cfd8c0,#4a4a4a 75%)}
.hero-quote{left:493px;top:209px;width:509px;height:145px;background:rgba(35,80,4,.75);padding:20px 22px;color:var(--white)}
.hero-quote h2{font:italic 700 16px "Roboto Condensed",Arial Narrow,sans-serif;text-transform:uppercase;margin-bottom:9px}
.hero-quote p{font-size:11px;line-height:15px}
.slider-tab{left:785px;top:410px;width:178px;height:44px;background:var(--white);border-radius:10px 10px 0 0;display:flex;justify-content:center;align-items:center;gap:10px}
.slider-tab span{width:15px;height:15px;border-radius:50%;background:#e2e2e2;box-shadow:inset 0 1px 2px rgba(0,0,0,.25)}
.slider-tab span.on{background:var(--leaf)}
.video{left:198px;top:493px;width:506px;height:128px;background:linear-gradient(#6b9fd6 0%,#a7c4e6 40%,#e0b21c 70%,#5e7a1c 100%)}
.play{left:425px;top:514px;width:52px;height:44px;border-radius:8px;background:rgba(0,0,0,.55)}
.video-caption{left:198px;top:573px;width:506px;height:38px;background:rgba(0,0,0,.55);color:var(--white);font:700 17px "Roboto Condensed",Arial Narrow,sans-serif;text-transform:uppercase;text-align:center;line-height:38px}
.section-title{font:700 19px "Roboto Condensed",Arial Narrow,sans-serif;color:var(--leaf);text-transform:uppercase}
.newsletter{left:729px;top:487px;width:273px}
.newsletter .section-title{padding-bottom:5px;border-bottom:1px solid #ddd}
.email{margin-top:9px;height:31px;border:1px solid #ccc;padding-left:8px;font-size:11px;line-height:29px;color:#999}
.note{margin-top:11px;font-size:10.5px;color:var(--muted)}
.submit{margin-top:12px;width:74px;height:22px;background:linear-gradient(var(--leaf-light),var(--leaf));color:var(--white);font:700 11px "Arimo",Arial,sans-serif;line-height:22px;text-align:center;text-transform:uppercase;border-radius:2px}
.rule{left:198px;top:643px;width:506px;height:1px;background:#e2e2e2}
.news{left:198px;top:652px;width:506px}
.date{font-size:10px;color:var(--muted);margin-top:10px}
.news h3{font:400 16px "Arimo",Arial,sans-serif;color:var(--leaf);margin:4px 0 5px}
.body{font-size:10.5px;line-height:14px;color:var(--muted)}
.more{font-size:10px;color:var(--ink);text-decoration:underline}
.testimonials{left:729px;top:652px;width:273px}
.testimonials .section-title{padding-bottom:5px;border-bottom:1px solid #ddd}
.quote{margin-top:10px}
.quote .more{display:block;margin-top:3px}
.foot-links{left:184px;top:930px;display:flex;gap:16px}
.foot-links a{color:var(--white);text-decoration:none;font:700 12px "Arimo",Arial,sans-serif}
.copyright{left:184px;top:960px;color:#bbb;font-size:9px}
.follow{left:852px;top:926px;color:var(--white);font:700 15px "Roboto Condensed",Arial Narrow,sans-serif;text-transform:uppercase}
.social{left:860px;top:953px;display:flex;gap:8px}
.social span{width:22px;height:22px;border-radius:3px;background:#3b72c4}
.social span:last-child{background:#d24a3a}
</style>
</head>
<body>
<div class="abs site-footer"></div>
<div class="abs page"></div>

<div class="abs brand"><span class="brand-dot"></span><span class="brand-name">Blue Lantern Hour</span></div>
<div class="abs account" style="left:885px">Login</div>
<div class="abs account" style="left:947px">Sign Up</div>

<nav class="abs nav">
  <a href="#" style="width:122px">Home</a>
  <a href="#" class="active" style="width:134px">The Way</a>
  <a href="#" style="width:173px">Live It</a>
  <a href="#" style="width:189px">Who Is He</a>
  <a href="#" style="width:214px;border-right:0">Contact Me</a>
</nav>

<section class="abs hero"></section>
<div class="abs hero-photo" role="img" aria-label="Photo of the coach holding a notebook beside a microphone"></div>
<div class="abs hero-quote">
  <h2>Lorem ipsum dolor sit amet, consectetuer adipiscing</h2>
  <p>Welcome to a brighter way of living. Our coaching sessions help you find clarity, purpose and daily joy. Join us for talks, seminars and personal guidance designed to lift your spirit and move your life forward with confidence.</p>
</div>
<div class="abs slider-tab"><span></span><span class="on"></span><span></span><span></span><span></span></div>

<div class="abs video" role="img" aria-label="Sunflower field under a blue sky, video preview"></div>
<svg class="abs play" viewBox="0 0 52 44"><polygon points="20,12 20,32 36,22" fill="#fff"/></svg>
<div class="abs video-caption">Lorem ipsum dolor sit amet, consectetuer adipiscing elit.</div>

<aside class="abs newsletter">
  <div class="section-title">Newsletter</div>
  <div class="email">Enter Your Email ID</div>
  <div class="note">Lorem ipsum dolor sit amet, consectetuer adipiscing elit.</div>
  <div class="submit">Submit</div>
</aside>

<div class="abs rule"></div>

<section class="abs news">
  <div class="section-title">Latest News</div>
  <div class="date">24.JUN 2012</div>
  <h3>Lorem ipsum dolor sit amet, consectetuer adipiscing elit.</h3>
  <p class="body">Every small step counts. This week we look at simple morning habits that set a calm, happy tone for the whole day ahead and help you stay focused on what truly matters to you.</p>
  <div class="date">24.JUN 2012</div>
  <h3>Lorem ipsum dolor sit amet, consectetuer adipiscing elit.</h3>
  <p class="body">Gratitude changes everything. Learn how writing three good things each evening can lift your mood, improve your sleep and bring a fresh sense of purpose to each new morning you wake up to.</p>
  <div style="text-align:right;margin-top:6px"><a class="more" href="#">read more..</a></div>
</section>

<section class="abs testimonials">
  <div class="section-title">Testimonials</div>
  <div class="quote"><p class="body">These sessions gave me the courage to change my career and finally follow my dream. I feel happier every day.</p><a class="more" href="#">- James Smith</a></div>
  <div class="quote"><p class="body">A warm, honest coach who truly listens. Each talk left me inspired and ready to take action.</p><a class="more" href="#">- James Smith</a></div>
  <div class="quote"><p class="body">Simple ideas that really work. My family has noticed the difference and so have I.</p><a class="more" href="#">- James Smith</a></div>
  <div style="text-align:right;margin-top:6px"><a class="more" href="#">read more..</a></div>
</section>

<nav class="abs foot-links"><a href="#">Home</a><a href="#">the way</a><a href="#">live it</a><a href="#">who is he</a><a href="#">Contact me</a></nav>
<div class="abs copyright">COPYRIGHT@2012 COMPANY ALL RIGHTS RESERVED</div>
<div class="abs follow">Follow us on</div>
<div class="abs social"><span></span><span></span><span></span><span></span></div>
</body>
</html>
```